Company identity deisgn should support 2 languages

I would like to get our company identity design
This includes the following only
Business Cards 2 languages Arabic and English
Email signature
Letterhead
Linkedin profile images
Attached is the logo in Ai format

Requirements
Must have
• For business card
Must have
Name and Adrees in arabic
Name and Address in english
You might use both side of the card
Should not have
• Any pictures other than the logo

```html
<!DOCTYPE html>
<html lang="en">
<head>
<meta charset="utf-8">
<title>Meridian Data Works – Stationery</title>
<link rel="stylesheet" href="https://fonts.googleapis.com/css2?family=Oswald:wght@300;400;500&family=Cairo:wght@300;400;600&display=swap">
<style>
  :root{
    --bg:#999999;
    --paper:#ffffff;
    --brand-blue:#1a75bc;
    --text-grey:#6d6e71;
    --text-dark:#58595b;
    --text-light:#a7a9ac;
  }
  *{margin:0;padding:0;box-sizing:border-box}
  html,body{width:1200px;height:1200px;overflow:hidden;background:var(--bg)}
  body{position:relative;font-family:'Oswald',sans-serif;font-weight:300;color:var(--text-grey)}

  .sheet{position:absolute;background:var(--paper);box-shadow:0 2px 6px rgba(0,0,0,.25);overflow:hidden}
  .letterhead{left:61px;top:142px;width:652px;height:922px}
  .card{width:372px;height:219px}
  .card--en{left:779px;top:242px}
  .card--ar{left:779px;top:528px}

  .brand{position:absolute;display:flex;align-items:center;gap:7px;
    font-family:'Oswald',sans-serif;font-weight:400;color:var(--brand-blue);letter-spacing:.04em;white-space:nowrap}
  .brand__dot{border-radius:50%;background:var(--brand-blue)}
  .letterhead .brand{right:60px;top:44px;font-size:20px}
  .letterhead .brand__dot{width:16px;height:16px}
  .card .brand{right:25px;top:28px;font-size:12.5px}
  .card .brand__dot{width:10px;height:10px}

  .letter-body{position:absolute;left:63px;top:181px;width:525px;font-size:10.4px;line-height:15.5px;text-align:justify}
  .letter-body p{margin-bottom:15.5px}
  .letter-body .salutation{margin-bottom:15px}

  .signature{position:absolute;left:63px;top:717px}
  .signature .name{font-weight:500;font-size:10.5px;color:var(--text-dark);text-transform:uppercase}
  .signature .role{font-size:9px}

  .letter-footer{position:absolute;left:39px;top:826px;font-size:12.5px;line-height:17px}
  .letter-footer .company{font-weight:500;font-size:10.5px;color:var(--text-dark);text-transform:uppercase;margin-top:3px;line-height:15px}
  .letter-footer .address{font-size:10px;line-height:14px}

  .card .person{position:absolute;left:24px;top:71px}
  .card .person .name{font-weight:500;font-size:12.5px;color:var(--text-dark);text-transform:uppercase;line-height:16px}
  .card .person .role{font-size:9px;line-height:13px}
  .card .contact{position:absolute;left:24px;top:134px;font-size:8.5px;line-height:13px}
  .card .web{position:absolute;left:24px;top:185px;font-size:8px}
  .card .office{position:absolute;right:25px;top:161px;text-align:right;font-size:8px;line-height:13px}
  .card .office .company{font-weight:500;font-size:8.5px;color:var(--text-dark);text-transform:uppercase}

  .card--ar .arabic{font-family:'Cairo',sans-serif}
  .card--ar .person .name{font-family:'Cairo',sans-serif;font-weight:600;font-size:12px;text-transform:none}
  .card--ar .person .role{font-family:'Cairo',sans-serif;color:var(--text-light);font-size:8.5px}
  .card--ar .office{direction:rtl;text-align:right;font-family:'Cairo',sans-serif;font-size:7.5px;line-height:13px;top:155px}
  .card--ar .office .company{font-family:'Cairo',sans-serif;font-weight:400;color:var(--text-dark);font-size:7.5px}
  .card--ar .office .street{color:var(--text-light)}
</style>
</head>
<body>

<section class="sheet letterhead">
  <div class="brand"><span class="brand__dot"></span>MERIDIAN DATA WORKS</div>

  <div class="letter-body">
    <p class="salutation">Dear Sir</p>
    <p>Lorem ipsum dolor sit amet, consetetur sadipscing elitr, sed diam nonumy eirmod tempor invidunt ut labore et dolore magna aliquyam erat, sed diam voluptua. At vero eos et accusam et justo duo dolores et ea rebum. Stet clita kasd gubergren, no sea takimata sanctus est Lorem ipsum dolor sit amet. Lorem ipsum dolor sit amet, consetetur sadipscing elitr, sed diam nonumy eirmod tempor invidunt ut labore et dolore magna aliquyam erat, sed diam voluptua. At vero eos et accusam et justo duo dolores et ea rebum. Stet clita kasd gubergren, no sea takimata sanctus est Lorem ipsum dolor sit amet. Lorem ipsum dolor sit amet, consetetur sadipscing elitr, sed diam nonumy eirmod tempor invidunt ut labore et dolore magna aliquyam erat, sed diam voluptua. At vero eos et accusam et justo duo dolores et ea rebum. Stet clita kasd gubergren, no sea takimata sanctus est Lorem ipsum dolor sit amet. Duis autem vel eum iriure dolor in hendrerit in vulputate velit esse molestie consequat, vel illum dolore eu feugiat nulla facilisis at vero eros et accumsan et iusto odio dignissim qui blandit praesent luptatum zzril delenit augue duis dolore te feugait nulla facilisi. Lorem ipsum dolor sit amet, consectetuer adipiscing elit, sed diam nonummy nibh euismod tincidunt ut laoreet dolore magna aliquam erat volutpat.</p>
    <p>Ut wisi enim ad minim veniam, quis nostrud exerci tation ullamcorper suscipit lobortis nisl ut aliquip ex ea commodo consequat. Duis autem vel eum iriure dolor in hendrerit in vulputate velit esse molestie consequat, vel illum dolore eu feugiat nulla facilisis at vero eros et accumsan et iusto odio dignissim qui blandit praesent luptatum zzril delenit augue duis dolore te feugait nulla facilisi. Nam liber tempor cum soluta nobis eleifend option congue nihil imperdiet doming id quod mazim placerat facer possim assum. Lorem ipsum dolor sit amet, consectetuer adipiscing elit, sed diam nonummy nibh euismod tincidunt ut laoreet dolore magna aliquam erat volutpat. Ut wisi enim ad minim veniam, quis nostrud exerci tation ullamcorper suscipit lobortis nisl ut aliquip ex ea commodo consequat. Duis autem vel eum iriure dolor in hendrerit in vulputate velit esse molestie consequat, vel illum dolore eu feugiat nulla facilisis.</p>
    <p>At vero eos et accusam et justo duo dolores et ea rebum. Stet clita kasd gubergren, no sea takimata sanctus est Lorem ipsum dolor sit amet. Lorem ipsum dolor sit amet, consetetur sadipscing elitr, sed diam nonumy eirmod tempor invidunt ut labore et dolore magna aliquyam erat, sed diam voluptua. At vero eos et accusam et justo duo dolores et ea rebum. Stet clita kasd gubergren, no sea takimata sanctus est Lorem ipsum dolor sit amet. Lorem ipsum dolor sit amet, consetetur sadipscing elitr, At accusam aliquyam diam diam dolore dolores duo eirmod eos erat, et nonumy sed tempor et et invidunt justo labore Stet clita ea et gubergren, kasd magna no rebum. sanctus sea sed takimata ut vero voluptua. est Lorem ipsum dolor sit amet. Lorem ipsum dolor sit amet, consetetur sadipscing elitr, sed diam nonumy eirmod tempor invidunt ut labore et dolore magna aliquyam erat.</p>
    <p>Consetetur sadipscing elitr, sed diam nonumy eirmod tempor invidunt ut labore et dolore magna aliquyam erat, sed diam voluptua. At vero eos et accusam et justo duo dolores et ea rebum. Stet clita kasd gubergren, no sea takimata sanctus est Lorem ipsum dolor sit amet. Lorem ipsum dolor sit amet, consetetur sadipscing elitr, sed diam nonumy eirmod tempor invidunt ut labore et dolore magna aliquyam erat, sed diam voluptua. At vero eos et accusam et justo duo dolores et ea rebum. Stet clita kasd gubergren, no sea takimata sanctus est Lorem ipsum dolor sit amet. Lorem ipsum dolor sit amet, consetetur sadipscing elitr, sed diam nonumy eirmod tempor invidunt ut labore et dolore magna aliquyam erat, sed diam voluptua. At vero eos et accusam et justo duo dolores et ea rebum. Stet clita kasd gubergren, no sea takimata sanctus est Lorem ipsum dolor sit amet.</p>
  </div>

  <div class="signature">
    <div class="name">Faris Almutairi</div>
    <div class="role">Business Development Director</div>
  </div>

  <div class="letter-footer">
    <div>M : 966 50 123 4567</div>
    <div>E : faris@meridianworks.sa &nbsp;|&nbsp; www.meridianworks.sa</div>
    <div class="company">Meridian Data Works</div>
    <div class="address">Tower 9, 12<sup>th</sup> Floor, King Fahd Rd. Dammam Saudi Arabia</div>
  </div>
</section>

<section class="sheet card card--en">
  <div class="brand"><span class="brand__dot"></span>MERIDIAN DATA WORKS</div>
  <div class="person">
    <div class="name">Faris Almutairi</div>
    <div class="role">Business Development Director</div>
  </div>
  <div class="contact">
    <div>M : 966 50 123 4567</div>
    <div>E : faris@meridianworks.sa</div>
  </div>
  <div class="web">www.meridianworks.sa</div>
  <div class="office">
    <div class="company">Meridian Data Works</div>
    <div>Tower 9, 12<sup>th</sup> Floor,</div>
    <div>King Fahd Rd. Dammam Saudi Arabia</div>
  </div>
</section>

<section class="sheet card card--ar">
  <div class="brand"><span class="brand__dot"></span>MERIDIAN DATA WORKS</div>
  <div class="person">
    <div class="name" lang="ar" dir="rtl">فارس المطيري</div>
    <div class="role" lang="ar" dir="rtl">مدير تطوير الأعمال</div>
  </div>
  <div class="contact">
    <div>M : 966 50 123 4567</div>
    <div>E : faris@meridianworks.sa</div>
  </div>
  <div class="web">www.meridianworks.sa</div>
  <div class="office" lang="ar">
    <div class="company">ميريديان لأعمال البيانات</div>
    <div>برج 9 الطابق 12</div>
    <div class="street">طريق الملك فهد، الدمام المملكة العربية السعودية</div>
  </div>
</section>

</body>
</html>
```